BLUE & AMBER SALVE TOPICAL BOX + LABELS TO MATCH

Hello ! I hope you're up to helping with my designs again. I appreciate all your help.
I have two topicals needing redesign.
Box + Label , once the box is together, we can slap the labels together easy.
I have CBD version and THC version of both these balms, so well start w THC, then lay out the CBD. It should be eaay with few minor differences.
PLEASE USE only tHE SMALL BOX TEMPLATE,
Anyway, once the boxes are complete, I need to revise the label to match the boxes.
1.
AMBER SALVE :
(this box color I would like orange, like a jack-o-lantern (i uploaded our current label so you can match it)
KORVEX logo outlined in Gold (on LID)
(I uploaded a picture of what the oulined logo looks like)
THC SYMBOL
AMBER SALVE (GOLD) (on Front)
HIGHLY NUTRITIOUS POWERFUL THC RELIEF
net wt. 2 oz (56 g)
SIDE PANEL :
ORGANIC INGREDIENTS : Butyrospermum Parkii Butter (Shea Butter), Persia Gratissima (Avocado) Oil, Simmondsia chinesis (Gold Jojoba) Oil , Vitus Vinifera (Grape) Seed Oil, Arnica montana (Arnica) and Symphytum officinalis (Comfrey Leaf) macerated in Sunflower Oil, Calophyllum inophyllum (Tamanu) Oil, Nigella sativa (Black Seed) Oil, Locally Harvested Beeswax, THC CANNABIS EXTRACT, Pure Cannabigerol (CBG), Proprietary Blend of Therapeutic Essential Oils (including but not limited to : Yarrow , Celery Seed , Tea Tree , Lavender , Helichrysum, Pine Scotch, Rosemary, Geranium), Tocopherol (Vitamin E, antioxidant )
Color is a Natural Result of Chamomile Steam-Distillation and May Vary in Intensity. Consistency can also Vary. For Optimal Preservation, Keep in a Cool, Dark Place. Fatty Acids may Naturally Aggregate when Exposed to Temperature Extremes Forming Beads. To Fix This, Use a Hair Dryer to Melt them Back to a Smooth Consistency.
BACK PANEL :
WARNING: THIS PRODUCT IS FOR USE BY INDIVIDUALS 21 YEARS OF AGE OR OLDER OR BY REGISTERED QUALIFYING PATIENTS ONLY. IT IS ILLEGAL TO DRIVE A MOTOR VEHICLE WHILE UNDER THE INFLUENCE OF MARIJUANA.
(Outlined Box )::
WARNING: USE BY PREGNANT OR BREASTFEEDING WOMEN OR BY WOMEN PLANNING TO BECOME PREGNANT, MAY RESULT IN FETAL INJURY, PRETERM BIRTH, LOW BIRTHWEIGHT, OR DEVELOPMENTAL PROBLEMS FOR THE CHILD.
KEEP OUT OF REACH OF CHILDREN.
CIVIC TOXIN RESPONSE BUREAU 1 800 555 0147
THE ACTUAL VALUE OF CANNABINOIDS MAY VARY FROM THE REPORTED VALUE BY +/- 10%
ACTIVATION TIME : 10 - 60 MINUTES
MADE IN A MARIJUANA FACILITY
PACKAGED BY
MILDRED’S HAZE Co.
KT-R-004817
www.FROSTLUMP.info
2.
TEAL SALVE
white box
KORVEX Gold out line, red w blue leaf
FRONT PANEL :
TEAL SALVE (blue)
net wt. 2 oz (56 g)
Ingredients : Butyrospermum Parkii Butter (Shea Butter), Aloe Barbadensis (Aloe Vera) Leaf Extract, Coco Nucifera (Coconut) Oil, THC CANNABIS EXTRACT, Cannabis Sativa Seed Oil, Pure Cannabidol (Hemp Extract), Prunes Armeniaca (Apricot) Kernal Oil, Hydrogenated Vegetable (Soybean) Oil, Prunus Amygdalus Dulcis (Sweet Almond Oil), Vitus Vinifera (Grape) Seed Oil, Macadamia Ternifolia Seed Oil, Daucus Carota (Carrot) Seed Oil, Proprietary Blend of Therapeutic Essential Oils (including but not limited to : Lavender, Chamomile), Tocopherol (Vitamin E, antioxidant)

```html
<!DOCTYPE html>
<html lang="en">
<head>
<meta charset="utf-8">
<title>Amber Salve – Small Box Dieline</title>
<link href="https://fonts.googleapis.com/css2?family=Poppins:wght@400;500;600&family=Anton&family=Roboto:wght@400&display=swap" rel="stylesheet">
<style>
  :root {
    --paper: #ffffff;
    --pumpkin: #f27822;
    --gold: #f3cf73;
    --ink-white: #ffffff;
    --cut: #1a1a1a;
    --bleed: #8fd27d;
    --dim: #2f5fae;
  }
  html, body { margin: 0; padding: 0; width: 1200px; height: 1200px; overflow: hidden; background: var(--paper); }
  .stage { position: relative; width: 1920px; height: 1920px; transform: scale(0.625); transform-origin: 0 0; }
  .dieline { position: absolute; left: 0; top: 0; width: 1920px; height: 1920px; }
  .panel-fill { fill: var(--pumpkin); }
  .cut { fill: none; stroke: var(--cut); stroke-width: 1.4; }
  .bleed { fill: none; stroke: var(--bleed); stroke-width: 1.2; }
  .dim-line { fill: none; stroke: var(--dim); stroke-width: 1; }
  .dim-label { font-family: "Roboto", Arial, sans-serif; font-size: 34px; fill: var(--dim); }

  .copy { position: absolute; font-family: "Poppins", Arial, sans-serif; color: var(--ink-white); font-size: 9.6px; line-height: 12.9px; letter-spacing: 0.1px; }
  .ingredients { left: 167px; top: 934px; width: 300px; text-align: justify; text-align-last: center; }
  .ingredients p { margin: 0 0 12px; }

  .brand { position: absolute; font-family: "Poppins", Arial, sans-serif; font-weight: 600; color: var(--gold); font-size: 30px; letter-spacing: 1px; text-align: center; width: 316px; }
  .brand-front { left: 471px; top: 978px; }
  .brand-lid { left: 471px; top: 748px; transform: rotate(180deg); }

  .product-name { position: absolute; left: 471px; top: 1026px; width: 316px; text-align: center; font-family: "Anton", Impact, sans-serif; font-size: 54px; line-height: 64px; color: var(--gold); letter-spacing: 0.5px; }
  .tagline { position: absolute; left: 471px; top: 1089px; width: 316px; text-align: center; font-family: "Poppins", Arial, sans-serif; font-size: 12.4px; color: var(--ink-white); }
  .net-wt { position: absolute; left: 471px; top: 1151px; width: 316px; text-align: center; font-family: "Poppins", Arial, sans-serif; font-size: 13.5px; color: var(--ink-white); }

  .back-panel { left: 797px; top: 935px; width: 293px; text-align: center; }
  .back-panel p { margin: 0; }
  .warning-box { border: 1.2px solid var(--ink-white); margin: 22px -2px 0; padding: 4px 6px 6px; }
  .keep-out { margin-top: 17px !important; }
  .poison { margin-top: 26px !important; }
  .poison strong { font-weight: 600; }

  .side-panel { left: 1104px; top: 978px; width: 308px; text-align: center; }
  .side-panel p { margin: 0 0 13px; }
  .packer { position: absolute; left: 1104px; top: 1120px; width: 308px; text-align: center; }
  .packer p { margin: 0; }
</style>
</head>
<body>
<div class="stage">
  <svg class="dieline" viewBox="0 0 1920 1920" xmlns="http://www.w3.org/2000/svg">
    <!-- printed areas -->
    <rect class="panel-fill" x="145" y="922" width="1370" height="263"/>
    <rect class="panel-fill" x="450" y="608" width="353" height="314"/>
    <rect class="panel-fill" x="1082" y="1185" width="353" height="320"/>

    <!-- bleed outline -->
    <path class="bleed" d="M450 608 V584 H458 V552 Q458 494 520 494 H738 Q800 494 800 552 V584 H803 V608"/>
    <path class="bleed" d="M450 754 H190 L162 862 L145 880 V922"/>
    <path class="bleed" d="M803 754 H1068 L1097 862 L1115 880 V908 H1416 L1515 935"/>
    <path class="bleed" d="M145 1185 V1200 L157 1215 L163 1356 H439 L467 1245 L485 1228 V1200 H772 V1228 L790 1245 L820 1356 H1082"/>
    <path class="bleed" d="M1435 1185 L1515 1170 M1435 1195 L1515 1175"/>
    <path class="bleed" d="M1082 1505 V1518 H1088 V1555 Q1088 1616 1150 1616 H1365 Q1430 1616 1430 1555 V1518 H1435 V1505"/>
    <path class="bleed" d="M145 922 H1515 M145 1185 H1515 M471 608 V1185 M787 608 V1185 M1100 922 V1505 M1416 922 V1505"/>

    <!-- cut & crease -->
    <path class="cut" d="M474 608 V560 Q474 510 524 510 H734 Q784 510 784 560 V608 M471 608 H516 V616 M787 608 H742 V616"/>
    <path class="cut" d="M471 608 V925 M787 608 V925"/>
    <path class="cut" d="M450 770 H202 L177 870 L160 886 V922 M450 770 L455 908 Q458 925 471 925"/>
    <path class="cut" d="M808 770 H1055 L1080 870 L1098 886 V922 M808 770 L803 908 Q800 925 787 925"/>
    <path class="cut" d="M1100 925 H1416 L1498 948 V1163 L1416 1185 M1416 925 V1185"/>
    <path class="cut" d="M160 1185 L174 1200 L179 1338 H426 L452 1240 L469 1223 V1185 H789 V1223 L806 1240 L832 1338 H1079 L1084 1200 Q1090 1185 1100 1185"/>
    <path class="cut" d="M1100 1185 V1500 M1416 1185 V1500 M1100 1500 H1145 V1493 M1416 1500 H1372 V1493"/>
    <path class="cut" d="M1104 1500 V1550 Q1104 1600 1154 1600 H1362 Q1412 1600 1412 1550 V1500"/>

    <!-- dimensions -->
    <path class="dim-line" d="M160 332 H778 M880 332 H1498 M160 326 V874 M1498 326 V935"/>
    <path class="dim-line" d="M188 324 L160 332 L188 340 M1470 324 L1498 332 L1470 340"/>
    <path class="dim-line" d="M160 413 H275 M357 413 H471 M471 413 H602 M656 413 H787 M787 413 H917 M970 413 H1100 M1100 413 H1232 M1285 413 H1416 M1498 413 H1555"/>
    <path class="dim-line" d="M188 405 L160 413 L188 421 M443 405 L471 413 L443 421 M499 405 L471 413 L499 421 M759 405 L787 413 L759 421 M815 405 L787 413 L815 421 M1072 405 L1100 413 L1072 421 M1128 405 L1100 413 L1128 421 M1388 405 L1416 413 L1388 421 M1526 405 L1498 413 L1526 421"/>
    <path class="dim-line" d="M471 406 V540 M787 406 V540 M1100 406 V880 M1416 406 V910"/>
    <path class="dim-line" d="M796 510 H1750 M1425 1600 H1750 M1743 510 V1035 M1743 1077 V1600 M1735 538 L1743 510 L1751 538 M1735 1572 L1743 1600 L1751 1572"/>
    <path class="dim-line" d="M1430 922 H1672 M1430 1187 H1672 M1666 922 V1035 M1666 1077 V1187 M1658 950 L1666 922 L1674 950 M1658 1159 L1666 1187 L1674 1159"/>
    <text class="dim-label" x="829" y="345" text-anchor="middle">242.4</text>
    <text class="dim-label" x="316" y="426" text-anchor="middle">56.4</text>
    <text class="dim-label" x="629" y="426" text-anchor="middle">57</text>
    <text class="dim-label" x="943" y="426" text-anchor="middle">57</text>
    <text class="dim-label" x="1258" y="426" text-anchor="middle">57</text>
    <text class="dim-label" x="1458" y="426" text-anchor="middle">15</text>
    <text class="dim-label" x="1666" y="1068" text-anchor="middle">48</text>
    <text class="dim-label" x="1745" y="1068" text-anchor="middle">197.6</text>
  </svg>

  <div class="brand brand-lid">KORVEX</div>

  <div class="copy ingredients">
    <p>ORGANIC INGREDIENTS : Butyrospermum Parkii Butter (Shea Butter), Persia Gratissima (Avocado) Oil, Simmondsia chinesis (Gold Jojoba) Oil , Vitus Vinifera (Grape) Seed Oil, Arnica montana (Arnica) and Symphytum officinalis (Comfrey Leaf) macerated in Sunflower Oil, Calophyllum inophyllum (Tamanu) Oil, Nigella sativa (Black Seed) Oil, Locally Harvested Beeswax, THC CANNABIS EXTRACT, Pure Cannabigerol (CBG), Proprietary Blend of Therapeutic Essential Oils (including but not limited to : Yarrow , Celery Seed , Tea Tree , Lavender , Helichrysum, Pine Scotch, Rosemary, Geranium), Tocopherol (Vitamin E, antioxidant )</p>
    <p>Color is a Natural Result of Chamomile Steam-Distillation and May Vary in Intensity. Consistency can also Vary. For Optimal Preservation, Keep in a Cool, Dark Place. Fatty Acids may Naturally Aggregate when Exposed to Temperature Extremes Forming Beads. To Fix This, Use a Hair Dryer to Melt them Back to a Smooth Consistency.</p>
  </div>

  <div class="brand brand-front">KORVEX</div>
  <div class="product-name">AMBER SALVE</div>
  <div class="tagline">HIGHLY NUTRITIOUS POWERFUL THC RELIEF</div>
  <div class="net-wt">Net Wt. 2 Oz (56 G)</div>

  <div class="copy back-panel">
    <p>WARNING: THIS PRODUCT IS FOR USE BY INDIVIDUALS 21 YEARS OF AGE OR OLDER OR BY REGISTERED QUALIFYING PATIENTS ONLY. IT IS ILLEGAL TO DRIVE A MOTOR VEHICLE WHILE UNDER THE INFLUENCE OF MARIJUANA.</p>
    <div class="warning-box">WARNING:<br>USE BY PREGNANT OR BREASTFEEDING WOMEN OR BY WOMEN PLANNING TO BECOME PREGNANT, MAY RESULT IN FETAL INJURY, PRETERM BIRTH, LOW BIRTHWEIGHT, OR DEVELOPMENTAL PROBLEMS FOR THE CHILD.</div>
    <p class="keep-out">KEEP OUT OF REACH OF CHILDREN.</p>
    <p class="poison">CIVIC TOXIN RESPONSE BUREAU <strong>1 800 555 0147</strong></p>
  </div>

  <div class="copy side-panel">
    <p>THE ACTUAL VALUE OF CANNABINOIDS MAY VARY FROM THE REPORTED VALUE BY +/- 10%</p>
    <p>ACTIVATION TIME : 10 - 60 MINUTES</p>
    <p>MADE IN A MARIJUANA FACILITY</p>
  </div>
  <div class="copy packer">
    <p>PACKAGED BY:</p>
    <p>MILDRED’S HAZE Co.</p>
    <p>KT-R-004817</p>
    <p>www.FROSTLUMP.info</p>
  </div>
</div>
</body>
</html>
```